Flyer for tutoring

The text should be presented in an engaging way to attract potential customers.
Colorfully designed
Around the edge, various objects related to school and the subjects (see text) should be visible.

```html
<!DOCTYPE html>
<html lang="de">
<head>
<meta charset="utf-8">
<title>Nachhilfe Flyer</title>
<link href="https://fonts.googleapis.com/css2?family=Poppins:ital,wght@0,400;0,500;0,600;0,700;0,800;1,500&display=swap" rel="stylesheet">
<style>
:root{
  --stage:#666769;
  --navy:#27307a;
  --navy-deep:#182566;
  --royal:#1d4595;
  --red:#e3271c;
  --red-dark:#b8171c;
  --orange:#f7a417;
  --yellow:#fde27a;
  --ink:#2a2a2a;
  --sky:#bfe3f5;
}
*{margin:0;padding:0;box-sizing:border-box}
html,body{width:1200px;height:1200px;overflow:hidden}
body{background:var(--stage);font-family:'Poppins',sans-serif;position:relative}
.flyer{
  position:absolute;left:190px;top:20px;width:820px;height:1160px;overflow:hidden;isolation:isolate;
  background:
    radial-gradient(ellipse 46% 44% at 50% 50%, #ffffff 0%, rgba(255,255,255,.85) 45%, rgba(255,255,255,0) 100%),
    radial-gradient(ellipse 62% 58% at 50% 48%, var(--sky) 0%, rgba(191,227,245,.6) 70%, rgba(191,227,245,0) 100%),
    linear-gradient(160deg, #f9b21c 0%, #fcd36a 30%, #fbe79a 55%, #c9de55 80%, #9ccd2e 100%);
}
.item{position:absolute;border-radius:14px;opacity:.9}
.cap{left:109px;top:78px;width:178px;height:150px;background:linear-gradient(160deg,#3a4356,#1f2636)}
.globe{left:639px;top:50px;width:150px;height:171px;background:linear-gradient(160deg,#5aa6dc,#3f7fc0)}
.calc{left:5px;top:183px;width:115px;height:90px;background:linear-gradient(160deg,#56627f,#3c4764)}
.pencil-top{left:399px;top:29px;width:125px;height:46px;background:linear-gradient(160deg,#7ccb62,#55b043)}
.backpack{left:696px;top:395px;width:122px;height:111px;background:linear-gradient(160deg,#ef6a3a,#3a5cb0)}
.book-left{left:0;top:464px;width:106px;height:97px;background:linear-gradient(160deg,#f7f8f3,#cfe6c9)}
.palette{left:0;top:649px;width:134px;height:93px;background:linear-gradient(160deg,#f9d65a,#efb834)}
.book-right{left:673px;top:635px;width:129px;height:93px;background:linear-gradient(160deg,#f8fafc,#f1cfcb)}
.ball{left:0;top:861px;width:88px;height:122px;background:linear-gradient(160deg,#f4f5f6,#c9ccd0)}
.pencil-right{left:694px;top:871px;width:101px;height:56px;background:linear-gradient(160deg,#f06a5c,#de3d30)}
.books{left:8px;top:1056px;width:153px;height:90px;background:linear-gradient(160deg,#5a9bd4,#4aa35a)}
.ruler{left:342px;top:1077px;width:154px;height:52px;background:linear-gradient(160deg,#f8cd4f,#f2b32c)}
.flask{left:697px;top:1000px;width:105px;height:139px;background:linear-gradient(160deg,#dbe6f3,#8a6ad0)}

.intro{position:absolute;left:230px;top:102px;width:420px;text-align:center;font-size:15px;font-weight:500;line-height:1.4;color:var(--ink)}
.title-box{position:absolute;left:203px;top:149px;width:414px;height:106px;border-radius:18px;background:linear-gradient(180deg,var(--navy-deep),var(--royal))}
.title-box span{position:absolute;left:0;right:0;top:18px;text-align:center;color:#fff;font-size:42px;font-weight:500;letter-spacing:.5px}
.ribbon{position:absolute;left:0;top:0;width:820px;height:420px}
.lead{position:absolute;left:160px;top:334px;width:500px;text-align:center;font-size:24px;font-weight:600;line-height:1.1;color:var(--navy)}
.lesson-head{position:absolute;left:119px;top:428px;width:568px;height:62px;border-radius:9px;background:linear-gradient(180deg,#fde46e,#f8ab17);text-align:center;padding-top:6px;line-height:1.25}
.lesson-head .h{display:block;font-size:22px;font-weight:700;color:var(--navy)}
.lesson-head .d{display:block;font-size:20px;font-weight:600;color:var(--red)}
.lesson-body{position:absolute;left:131px;top:490px;width:556px;height:108px;border-radius:0 0 10px 10px;background:linear-gradient(180deg,rgba(255,255,255,.9),#fde9a6 60%,#f9c74a);text-align:center;font-size:15.3px;line-height:1.33;color:var(--ink);padding:10px 6px 0;white-space:nowrap}
.rule{position:absolute;height:1.5px;background:var(--navy)}
.r1{left:134px;top:615px;width:551px}
.r2{left:134px;top:775px;width:551px}
.r3{left:156px;top:1025px;width:506px}
.r4{left:156px;top:1062px;width:506px}
.promise{position:absolute;left:150px;top:624px;width:520px;text-align:center;font-size:17.5px;font-weight:600;line-height:1.3;color:var(--navy)}
.goal{position:absolute;left:161px;top:681px;width:495px;height:77px;border-radius:8px;background:linear-gradient(180deg,#fdf0bb,#f9c437);text-align:center;font-size:29px;font-weight:600;line-height:1.05;color:var(--navy);padding-top:8px}
.about{position:absolute;left:117px;top:799px;width:620px;font-size:15.6px;line-height:1.3;color:var(--ink);white-space:nowrap}
.about .label{position:relative;z-index:0;font-weight:700;color:#1f1f1f;padding:0 14px 0 0;margin-right:14px}
.about .label::before{content:"";position:absolute;left:-18px;right:-4px;top:0;bottom:-2px;background:var(--orange);transform:skewX(-14deg);z-index:-1;opacity:.9}
.about em.subjects{color:var(--red);font-weight:500}
.about .math{display:block;margin-top:6px;color:var(--navy);font-style:italic;font-weight:500}
.contact-title{position:absolute;left:250px;top:906px;width:320px;text-align:center;font-size:18px;font-weight:600;color:var(--navy);z-index:0}
.contact-title::before{content:"";position:absolute;left:12px;right:12px;top:4px;bottom:2px;background:#fbd13c;transform:skewX(-12deg);z-index:-1}
.contact{position:absolute;left:118px;top:941px;width:578px;height:39px;border-radius:20px;border:2px solid #a6182c;background:#fff;display:flex;overflow:hidden}
.contact .mail{width:378px;height:100%;background:linear-gradient(90deg,#1c1a5a,#3c1f5e 55%,#a8182c);border-radius:0 20px 20px 0;display:flex;align-items:center;gap:12px;padding-left:20px;color:#fff;font-size:18px}
.contact .phone{flex:1;display:flex;align-items:center;gap:10px;padding-left:16px;color:#1a1a1a;font-size:18.5px;font-weight:700}
.reach{position:absolute;left:200px;top:985px;width:420px;text-align:center;font-size:17px;color:var(--ink)}
.bye{position:absolute;left:156px;top:1032px;width:506px;text-align:center;font-size:15.5px;font-style:italic;font-weight:500;color:var(--red-dark)}
</style>
</head>
<body>
<main class="flyer">
  <div class="item cap" role="img" aria-label="Illustration eines Doktorhuts"></div>
  <div class="item globe" role="img" aria-label="Illustration eines Globus"></div>
  <div class="item calc" role="img" aria-label="Illustration eines Taschenrechners"></div>
  <div class="item pencil-top" role="img" aria-label="Illustration eines grünen Bleistifts"></div>
  <div class="item backpack" role="img" aria-label="Illustration eines Schulrucksacks"></div>
  <div class="item book-left" role="img" aria-label="Illustration eines offenen Buchs"></div>
  <div class="item palette" role="img" aria-label="Illustration einer Malpalette"></div>
  <div class="item book-right" role="img" aria-label="Illustration eines offenen Hefts"></div>
  <div class="item ball" role="img" aria-label="Illustration eines Fussballs"></div>
  <div class="item pencil-right" role="img" aria-label="Illustration eines roten Bleistifts"></div>
  <div class="item books" role="img" aria-label="Illustration eines Bücherstapels"></div>
  <div class="item ruler" role="img" aria-label="Illustration eines Lineals mit Büroklammern"></div>
  <div class="item flask" role="img" aria-label="Illustration eines Erlenmeyerkolbens"></div>

  <p class="intro">Möchtest du dich gerne in der Schule<br>verbessern und suchst eine</p>
  <div class="title-box"><span>Professionelle</span></div>

  <svg class="ribbon" viewBox="0 0 820 420">
    <path d="M128,283 L64,300 L92,338 L64,376 L128,350 Z" fill="var(--red)"/>
    <path d="M692,283 L756,300 L728,338 L756,376 L692,350 Z" fill="var(--red)"/>
    <path d="M106,300 L128,350 L128,320 Z" fill="var(--red-dark)"/>
    <path d="M714,300 L692,350 L692,320 Z" fill="var(--red-dark)"/>
    <path d="M106,272 Q410,170 714,272 L714,328 Q410,226 106,328 Z" fill="#ea3b22"/>
    <path id="ribbonLine" d="M106,318 Q410,216 714,318" fill="none"/>
    <text font-family="Poppins, sans-serif" font-weight="800" font-size="26" fill="#fff" letter-spacing="0.6">
      <textPath href="#ribbonLine" startOffset="50%" text-anchor="middle">NACHHILFELEHRERIN / LERNCOACH ?</textPath>
    </text>
  </svg>

  <p class="lead">Dann lass es uns doch<br>mal versuchen!</p>

  <div class="lesson-head">
    <span class="h">Die erste Lektion – die Kennenlernlektion</span>
    <span class="d">– dauert ca. 30 Minuten.</span>
  </div>
  <p class="lesson-body">Sie ist kostenlos. Denn wir müssen ja sicher gehen, dass wir uns<br>verstehen und leiden können. Bei unserem ersten Treffen legen<br>wir auch fest, woran wir arbeiten werden und wann die<br>Nachhilfe in deine Agenda passt.</p>

  <div class="rule r1"></div>
  <p class="promise">Wenn der erste Eindruck stimmt, dann legen wir los,<br>und bald schon werden</p>
  <div class="goal">deine Motivation und deine<br>Noten besser und besser!</div>
  <div class="rule r2"></div>

  <p class="about"><span class="label">Zu meiner Person:</span>Ich wohne hier in der Siedlung am Lindenweg<br>und bin ausgebildete und sehr erfahrene Sekundar- und Primarlehrerin in<br>den Fächern Deutsch, <em class="subjects">Französisch, Englisch und Geschichte.</em>
    <span class="math">(Auf Wunsch auch Mathe-Nachhilfe möglich.)</span></p>

  <p class="contact-title">Meine Kontaktdaten:</p>
  <div class="contact">
    <div class="mail">
      <svg width="26" height="18" viewBox="0 0 26 18" aria-hidden="true"><rect x="1" y="1" width="24" height="16" fill="#f7b21b"/><path d="M1,1 L13,10 L25,1" fill="none" stroke="#1c1a5a" stroke-width="1.6"/></svg>
      <span>lena.vogt@postfach-mail.ch</span>
    </div>
    <div class="phone">
      <svg width="20" height="20" viewBox="0 0 24 24" aria-hidden="true"><path d="M6.6 10.8a15 15 0 0 0 6.6 6.6l2.2-2.2a1 1 0 0 1 1-.25 11.4 11.4 0 0 0 3.6.57 1 1 0 0 1 1 1V20a1 1 0 0 1-1 1A17 17 0 0 1 3 4a1 1 0 0 1 1-1h3.5a1 1 0 0 1 1 1c0 1.25.2 2.45.57 3.6a1 1 0 0 1-.25 1z" fill="#b3182a"/></svg>
      <span>076 000 41 27</span>
    </div>
  </div>
  <p class="reach">(nachmittags fast immer erreichbar)</p>

  <div class="rule r3"></div>
  <p class="bye">Ich freue mich auf deine Kontaktaufnahme! Bis bald!</p>
  <div class="rule r4"></div>
</main>
</body>
</html>
```